Bramblewick Dill Pickles needs your smart gourmet Design

Looking for a smart design for a dill pickle jar container. The text
Bramblewick Dill Pickles.
Simply Garden Crisp.

A tasty reason to raid the refrigerator.

Target Market(s)

Foodies, farmers market types.

Font styles to use
Serif
Sans Serif

Colors

Designer to choose colors to be used in the design.

Requirements
Must have
• Attractive design to entice foodies to buy my Pickles. Not cluttered, easy to read.
Nice to have
• Pickles, garlic. Modern.
Should not have
• Clutter. No script text.

```html
<!DOCTYPE html>
<html lang="en">
<head>
<meta charset="utf-8">
<title>Bramblewick Dill Pickles – Jar Label</title>
<link rel="stylesheet" href="https://fonts.googleapis.com/css2?family=Oswald:wght@300;500;600&display=swap">
<style>
  :root {
    --backdrop: #232523;
    --label-green: #7daf3f;
    --band-black: #111111;
    --paper-white: #f2f2f2;
    --ink-dark: #151515;
    --ink-grey: #7a7a7a;
    --pickle-light: #a9c94a;
    --pickle-dark: #4d6a1c;
    --badge-green: #3f7a2a;
  }
  * { margin: 0; padding: 0; box-sizing: border-box; }
  html, body {
    width: 1200px; height: 988px; overflow: hidden;
    background: var(--backdrop);
    font-family: "Oswald", sans-serif;
  }
  .label {
    position: absolute; left: 150px; top: 94px;
    width: 900px; height: 800px;
    background: var(--label-green);
    overflow: hidden;
  }
  .label__top-band {
    position: absolute; left: 0; top: 0; width: 100%; height: 50px;
    background: var(--band-black);
  }
  .label__wave { position: absolute; left: 0; top: 0; width: 900px; height: 800px; }
  .label__title {
    position: absolute; left: 80px; top: 80px;
    line-height: 1;
  }
  .label__brand {
    display: block;
    font-weight: 600; font-size: 96px; letter-spacing: -1px;
    color: var(--ink-dark);
  }
  .label__product {
    display: block; margin-top: 14px;
    font-weight: 300; font-size: 84px; letter-spacing: -1px;
    color: var(--paper-white);
  }
  .label__mark {
    position: absolute; left: 660px; top: 110px;
    width: 210px; height: 210px; border-radius: 50%;
    background: var(--paper-white);
    display: flex; align-items: center; justify-content: center;
  }
  .label__mark-name {
    font-weight: 600; font-size: 30px; color: var(--ink-dark);
  }
  .label__photo {
    position: absolute; left: 70px; top: 420px;
    width: 380px; height: 230px; border-radius: 110px;
    background: radial-gradient(ellipse at 40% 40%, var(--pickle-light), var(--pickle-dark));
  }
  .label__badge {
    position: absolute; left: 700px; top: 505px;
    width: 110px; height: 110px; border-radius: 50%;
    background: var(--badge-green);
    border: 4px solid var(--ink-dark);
    box-shadow: inset 0 0 0 4px var(--paper-white);
  }
  .label__tagline {
    position: absolute; left: 0; width: 100%; top: 655px;
    text-align: center;
    font-weight: 500; font-size: 40px; letter-spacing: 1px;
    color: var(--ink-grey);
  }
  .label__bottom-band {
    position: absolute; left: 0; bottom: 0; width: 100%; height: 80px;
    background: var(--band-black);
    border-top: 3px solid var(--paper-white);
    outline: 6px solid var(--band-black);
    display: flex; align-items: center; justify-content: center;
  }
  .label__weight {
    font-weight: 500; font-size: 30px; color: var(--paper-white);
  }
</style>
</head>
<body>
  <main class="label">
    <svg class="label__wave" viewBox="0 0 900 800" aria-hidden="true">
      <path d="M0 520 C 180 700, 420 640, 620 520 S 860 360, 900 380 L 900 800 L 0 800 Z" fill="var(--paper-white)"/>
    </svg>
    <div class="label__top-band"></div>

    <h1 class="label__title">
      <span class="label__brand">BRAMBLEWICK</span>
      <span class="label__product">DILL PICKLES</span>
    </h1>

    <div class="label__mark">
      <span class="label__mark-name">Bramblewick</span>
    </div>

    <div class="label__photo" role="img" aria-label="Photo of two dill pickles with a water splash, dill flower and peppercorns"></div>

    <div class="label__badge" role="img" aria-label="Natural product seal"></div>

    <p class="label__tagline">SIMPLY GARDEN CRISP</p>

    <div class="label__bottom-band">
      <p class="label__weight">NET WEIGHT 250G(8,87OZ)</p>
    </div>
  </main>
</body>
</html>
```